Blog Header Design + 2 Buttons + Colortheme

Hello,
I am looking for a fresh and catchy design for this blog project.
It can have a simplistic touch but I am open to all ideas which fit to the concept.
Please have a look at the pictures I've uploaded.
The website is called
http://www.wtwhn-blog.net
it is a blog which presents weird or extraordinary products. The URL is short for the german phrase "Was Toll Wäre Hier Nun?" it means "How cool is that?". Where "Geil" has the meaning of "Cool".
So yea, that is basically the idea of what it should stand for.
What I need is:
- a colortheme for the website
- a logo or banner at the top of the homesite (see the picture of the text I uploaded, if you could write it in this kind of deign that would look nice I guess)
- buttons for the product elements of the homesite and on the productdetail pages ("Toll!" Button and Price Button/Sign)
- background design (can fit the design idea but shouldnt be too distracting)
- if it is needed by or serves the design, the menu can be changed as well, but it can also stay as it is
optional for a complete set is needed:
- a favicon that fits the theme
- a facebook cover and profile picture
If you have any further questions please let know and I will respond to you as soon as possible.
Again, I am open to ALL design ideas for the whole website concept and would be glad to find a long term deign partner for other projects as well. THANK YOU!

```html
<!DOCTYPE html>
<html lang="en">
<head>
<meta charset="utf-8">
<title>Was Toll Wäre Hier Nun?</title>
<link rel="stylesheet" href="https://fonts.googleapis.com/css2?family=Arimo:wght@400;700&family=Lato:wght@700;900&family=Open+Sans:wght@400;600&display=swap">
<style>
  :root {
    --page-bg: #f1f1f1;
    --white: #ffffff;
    --brand-green: #3cb34a;
    --nav-green: #8cb92e;
    --brand-orange: #f29a1f;
    --ink: #111111;
    --muted: #8a8a8a;
    --line: #e4e4e4;
    --icon-grey: #c9c9c9;
    --sun-light: #fff8c8;
    --sun-deep: #fde98a;
  }
  * { box-sizing: border-box; margin: 0; padding: 0; }
  html, body { width: 1200px; height: 983px; overflow: hidden; }
  body { background: var(--page-bg); font-family: "Arimo", Arial, sans-serif; color: var(--ink); position: relative; }

  .site-name { position: absolute; left: 172px; top: 40px; font-family: "Lato", sans-serif; font-weight: 900; color: var(--brand-green); font-size: 27px; line-height: 29px; letter-spacing: -0.5px; }

  .search { position: absolute; left: 686px; top: 34px; display: flex; }
  .search-field { width: 158px; height: 30px; background: var(--white); border: 1px solid #d8d8d8; border-radius: 3px 0 0 3px; font-size: 11px; color: #aaa; padding: 8px 7px; }
  .search-button { width: 30px; height: 30px; background: var(--icon-grey); border-radius: 0 3px 3px 0; display: flex; align-items: center; justify-content: center; }
  .social { position: absolute; top: 34px; display: flex; gap: 4px; left: 877px; }
  .social-slot { width: 30px; height: 30px; background: var(--icon-grey); border-radius: 3px; }

  .main-nav { position: absolute; top: 124px; left: 0; width: 1200px; height: 18px; font-size: 14.5px; font-weight: 700; }
  .main-nav a { position: absolute; color: var(--ink); text-decoration: none; white-space: nowrap; }
  .main-nav a.is-current { color: var(--nav-green); }
  .rule-dotted { position: absolute; height: 0; border-top: 2px dotted #dcdcdc; }

  .hero { position: absolute; left: 159px; top: 162px; width: 881px; height: 360px; background: radial-gradient(ellipse at center, var(--sun-light) 0%, var(--sun-deep) 100%); display: flex; flex-direction: column; align-items: center; justify-content: center; }
  .hero-name { font-family: "Lato", sans-serif; font-weight: 900; color: var(--brand-green); font-size: 76px; line-height: 78px; text-align: center; letter-spacing: -1px; }
  .hero-strip { position: absolute; left: 159px; top: 522px; width: 881px; height: 62px; background: var(--white); border-bottom: 1px solid var(--line); }
  .hero-strip p { position: absolute; left: 145px; top: 16px; font-size: 26px; letter-spacing: 0.2px; }
  .hero-strip strong { font-weight: 700; }

  .section-title { position: absolute; left: 156px; top: 629px; font-family: "Open Sans", sans-serif; font-weight: 600; font-size: 18px; }
  .slider-arrows { position: absolute; left: 1008px; top: 633px; display: flex; gap: 3px; }
  .slider-arrows span { width: 16px; height: 16px; background: var(--nav-green); border-radius: 2px; display: flex; align-items: center; justify-content: center; }

  .product-card { position: absolute; top: 667px; width: 208px; height: 330px; background: var(--white); border: 1px solid #e9e9e9; }
  .product-photo { position: absolute; left: 6px; top: 6px; width: 194px; height: 148px; }
  .product-card h3 { position: absolute; left: 10px; top: 186px; font-family: "Open Sans", sans-serif; font-weight: 400; font-size: 13px; }
  .product-card p { position: absolute; left: 10px; top: 210px; font-family: "Open Sans", sans-serif; font-size: 8.5px; color: var(--muted); }
  .card-divider { position: absolute; left: 0; width: 100%; border-top: 1px solid var(--line); }
  .like-button { position: absolute; left: 18px; top: 283px; font-family: "Lato", sans-serif; font-weight: 900; font-size: 17px; color: var(--brand-green); }
  .price-tag { position: absolute; right: 17px; top: 283px; font-family: "Lato", sans-serif; font-weight: 900; font-size: 17px; color: var(--brand-orange); }
</style>
</head>
<body>
  <header>
    <div class="site-name">WAS TOLL WÄRE<br>HIER NUN?</div>
    <div class="search">
      <div class="search-field">Search...</div>
      <div class="search-button">
        <svg width="18" height="18" viewBox="0 0 18 18"><circle cx="7" cy="7" r="5" fill="none" stroke="#fff" stroke-width="2.5"/><line x1="10.5" y1="10.5" x2="16" y2="16" stroke="#fff" stroke-width="3" stroke-linecap="round"/></svg>
      </div>
    </div>
    <div class="social">
      <span class="social-slot"></span><span class="social-slot"></span><span class="social-slot"></span><span class="social-slot"></span><span class="social-slot"></span>
    </div>
    <nav class="main-nav">
      <a class="is-current" style="left:115px">HOME</a>
      <a style="left:186px">TECHNOLOGY</a>
      <a style="left:311px">FUN &amp; GAMES</a>
      <a style="left:436px">CLOTHING &amp; ACCESSORIES</a>
      <a style="left:640px">HOME &amp; OFFICE</a>
      <a style="left:762px">FOOD &amp; DRINK</a>
      <a style="left:880px">OTHER</a>
    </nav>
    <div class="rule-dotted" style="left:159px; top:154px; width:881px"></div>
  </header>

  <section class="hero" role="img" aria-label="Sunburst banner with the blog name">
    <div class="hero-name">WAS TOLL WÄRE<br>HIER NUN?</div>
  </section>
  <div class="hero-strip"><p>CHECK OUT THESE <strong>AMAZING PRODUCTS</strong>!</p></div>

  <h2 class="section-title">RECENT PRODUCTS</h2>
  <div class="rule-dotted" style="left:332px; top:641px; width:670px"></div>
  <div class="slider-arrows">
    <span><svg width="6" height="8" viewBox="0 0 6 8"><path d="M5 0L1 4l4 4" fill="none" stroke="#fff" stroke-width="1.5"/></svg></span>
    <span><svg width="6" height="8" viewBox="0 0 6 8"><path d="M1 0l4 4-4 4" fill="none" stroke="#fff" stroke-width="1.5"/></svg></span>
  </div>

  <article class="product-card" style="left:158px">
    <div class="product-photo" role="img" aria-label="Photo of white underpants" style="background:linear-gradient(160deg,#ffffff,#e9e2d6)"></div>
    <div class="card-divider" style="top:171px"></div>
    <h3>Safe Dirty Underpants</h3>
    <p>Informtaion about the product goes here.</p>
    <div class="card-divider" style="top:274px"></div>
    <span class="like-button">TOLL!</span>
    <span class="price-tag">$29.90</span>
  </article>

  <article class="product-card" style="left:384px">
    <div class="product-photo" role="img" aria-label="Photo of a child drinking through colourful connected straws" style="background:linear-gradient(135deg,#e7ece8,#9cc79a 55%,#e39a6a)"></div>
    <div class="card-divider" style="top:171px"></div>
    <h3>Straw Kit</h3>
    <p>Informtaion about the product goes here.</p>
    <div class="card-divider" style="top:274px"></div>
  </article>

  <article class="product-card" style="left:610px">
    <div class="product-photo" role="img" aria-label="Photo of clothes hanging on a line with bat-shaped clothespins" style="background:linear-gradient(90deg,#5f7f48,#3e4a5a 45%,#e9484a 80%,#6d8f4a)"></div>
    <div class="card-divider" style="top:171px"></div>
    <h3>Bat Clothespins</h3>
    <p>Informtaion about the product goes here.</p>
    <div class="card-divider" style="top:274px"></div>
  </article>

  <article class="product-card" style="left:834px">
    <div class="product-photo" role="img" aria-label="Photo of a jar of amber jam" style="background:radial-gradient(ellipse at center,#c98a32 0%,#e8cf9a 45%,#ffffff 72%)"></div>
    <div class="card-divider" style="top:171px"></div>
    <h3>Pus Jam</h3>
    <p>Informtaion about the product goes here.</p>
    <div class="card-divider" style="top:274px"></div>
  </article>
</body>
</html>
```